loft 17 design

We are needing a website built for our company. We are based in the Dallas/Ft. Worth area providing staging for realtors, occupied staging, apartments, builders and hospitality industry ( Roam Pods .) Have been in the design and furniture industry for 35+ years, looking to expand our services to the area. Here Are some of the buzzword used for staging. Turn properties into dream spaces. Staging preparing property for sale.
Design services offered for new construction . We want to incorporate our tag line Turning you property into a dream Space .
interior and home design
Coded - Design and coding required
2 page

```html
<!DOCTYPE html>
<html lang="en">
<head>
<meta charset="utf-8">
<title>Loft 17 Design — Staging and Interior Design</title>
<link href="https://fonts.googleapis.com/css2?family=Poppins:wght@300;400;500;600;700&display=swap" rel="stylesheet">
<style>
:root{
  --blue:#0b57b5;
  --blue-dark:#08479a;
  --blue-pale:#dbe6f5;
  --ink:#141414;
  --grey:#6b6b6b;
  --footer:#1e1f22;
  --white:#ffffff;
}
*{box-sizing:border-box;margin:0;padding:0}
html,body{width:1200px;height:3639px;overflow:hidden}
body{font-family:'Poppins',sans-serif;color:var(--ink);background:var(--white);position:relative}
.abs{position:absolute}

/* hero */
.hero{position:absolute;left:0;top:0;width:1200px;height:680px;overflow:hidden}
.hero-photo{position:absolute;inset:0;background:
  radial-gradient(ellipse at 15% 30%,#6f8a55 0,transparent 35%),
  radial-gradient(ellipse at 85% 35%,#7d9561 0,transparent 30%),
  radial-gradient(ellipse at 55% 60%,#2f5f4c 0,transparent 28%),
  linear-gradient(180deg,#eef0ea 0%,#e3e2da 45%,#b89c7e 75%,#8a6a4d 100%)}
.hero-wave{position:absolute;left:0;top:560px;width:1200px;height:120px}
.brand{position:absolute;font-weight:700;letter-spacing:2px;line-height:1.05;text-transform:uppercase}
.brand-hero{left:134px;top:40px;font-size:30px;color:var(--ink)}
.brand-dot{display:inline-block;width:14px;height:14px;border-radius:50%;background:currentColor;margin-right:10px;vertical-align:3px}
.topbar{position:absolute;top:8px;right:113px;display:flex;gap:34px;font-size:15px;font-weight:500;align-items:center}
.topbar span{display:flex;align-items:center;gap:14px}
.ico-circle{width:30px;height:30px;border-radius:50%;background:var(--ink);display:inline-flex;align-items:center;justify-content:center}
.nav{position:absolute;top:64px;right:113px;display:flex;gap:30px;font-size:15px;font-weight:500}
.hero-panel{position:absolute;left:113px;top:179px;width:672px;height:298px;background:rgba(255,255,255,.42)}
.hero-title{position:absolute;left:112px;top:222px;font-size:37px;font-weight:600;line-height:54px;text-transform:uppercase}
.btn{position:absolute;display:flex;align-items:center;justify-content:center;border-radius:40px;font-weight:600;font-size:20px}
.btn-blue{background:var(--blue);color:var(--white)}
.btn-white{background:var(--white);color:var(--blue)}

/* section headings */
.h2{position:absolute;left:0;width:1200px;text-align:center;font-size:33px;font-weight:600;text-transform:uppercase}
.arrows{position:absolute;width:56px;height:16px}

/* services */
.services-intro{position:absolute;left:200px;top:818px;width:800px;text-align:center;font-size:21px;line-height:31px}
.service{position:absolute;top:900px;width:300px;text-align:center}
.service-glow{width:290px;height:260px;margin:0 auto;border-radius:50%;display:flex;align-items:center;justify-content:center;
  background:radial-gradient(circle,rgba(11,87,181,.55) 0,rgba(11,87,181,.25) 45%,rgba(11,87,181,0) 70%)}
.service-ring{width:128px;height:128px;border-radius:50%;background:var(--white);display:flex;align-items:center;justify-content:center}
.service-core{width:112px;height:112px;border-radius:50%;background:var(--blue-pale);display:flex;align-items:center;justify-content:center}
.service-title{margin-top:25px;font-size:17px;font-weight:500;color:var(--blue)}
.service-text{margin:14px auto 0;width:170px;font-size:14.5px;line-height:26px;color:var(--grey)}

/* about */
.about{position:absolute;left:0;top:1402px;width:1200px;height:521px;background:var(--blue)}
.about-glow{position:absolute;left:103px;top:20px;width:480px;height:460px;border-radius:50%;
  background:radial-gradient(circle,rgba(255,255,255,.55) 0,rgba(255,255,255,.25) 40%,rgba(255,255,255,0) 68%)}
.brand-about{left:240px;top:205px;font-size:44px;color:var(--white);text-align:center}
.about-title{position:absolute;right:113px;top:88px;font-size:34px;font-weight:600;color:var(--white)}
.about-text{position:absolute;right:113px;top:155px;width:390px;text-align:right;font-size:15.5px;line-height:24.5px;color:var(--white);font-weight:300}

/* years band */
.band{position:absolute;left:0;top:1923px;width:1200px;height:195px;
  background:linear-gradient(90deg,#1d2420 0%,#3a3f3a 30%,#2b2e2c 60%,#3b3f3a 100%)}
.band-badge{position:absolute;left:543px;top:17px;width:114px;height:114px;border-radius:50%;background:var(--white)}
.band-text{position:absolute;left:0;width:1200px;top:146px;text-align:center;color:var(--white);font-size:20px;font-weight:600;text-transform:uppercase}

/* gallery */
.photo{position:absolute}

/* blogs */
.blogs{position:absolute;left:0;top:2742px;width:1200px;height:552px;
  background:linear-gradient(180deg,#1d5fba 0%,#0b57b5 50%,#0a4ea8 100%)}
.blog-card{position:absolute;top:145px;width:484px;height:318px;background:#eef1f7}
.blog-photo{position:absolute;left:8px;top:8px;width:468px;height:158px}
.blog-date{position:absolute;left:-20px;top:58px;width:132px;height:114px;background:var(--blue);border:5px solid var(--white);
  color:var(--white);font-size:22px;font-weight:500;text-align:center;line-height:32px;padding-top:20px}
.blog-text{position:absolute;left:28px;top:218px;width:440px;font-size:15.5px;line-height:24.5px;color:#233}

/* footer */
.footer{position:absolute;left:0;top:3294px;width:1200px;height:345px;background:var(--footer);color:var(--white)}
.brand-footer{left:116px;top:55px;font-size:34px;color:var(--white)}
.foot-contact{position:absolute;left:116px;font-size:16px;display:flex;align-items:center;gap:26px}
.foot-ico{width:32px;height:32px;border-radius:50%;background:var(--white);display:inline-flex;align-items:center;justify-content:center}
.foot-col{position:absolute;top:65px}
.foot-col h3{font-size:22px;font-weight:400;margin-bottom:12px}
.foot-col p{font-size:15.5px;line-height:24px}
.social{position:absolute;left:991px;width:40px;height:40px;border-radius:50%;border:2px solid var(--white)}
.copyright{position:absolute;left:0;width:1200px;top:310px;text-align:center;font-size:15.5px}
</style>
</head>
<body>

<header class="hero">
  <div class="hero-photo" role="img" aria-label="Bright living room with a green sofa, wooden side table and many house plants"></div>
  <svg class="hero-wave" viewBox="0 0 1200 120" preserveAspectRatio="none" aria-hidden="true">
    <path d="M0 20 Q520 65 940 110 L1200 30 L1200 120 L0 120 Z" fill="#0b57b5"/>
    <path d="M0 22 Q500 80 900 100 Q930 102 960 95 L1200 55 L1200 120 L0 120 Z" fill="#ffffff"/>
    <path d="M940 110 L1200 30 L1200 55 Q1080 85 960 95 Z" fill="#0b57b5"/>
  </svg>

  <div class="brand brand-hero"><span class="brand-dot"></span>Loft 17<br>Design</div>

  <div class="topbar">
    <span><i class="ico-circle"><svg width="14" height="12" viewBox="0 0 14 12"><rect x="1" y="1" width="12" height="10" rx="1" fill="none" stroke="#fff" stroke-width="1.6"/><path d="M1 2 L7 7 L13 2" fill="none" stroke="#fff" stroke-width="1.6"/></svg></i>hello@loft17studio.com</span>
    <span><i class="ico-circle"><svg width="14" height="14" viewBox="0 0 24 24"><path d="M6.6 10.8a15 15 0 006.6 6.6l2.2-2.2a1 1 0 011-.25 11 11 0 003.5.56 1 1 0 011 1V20a1 1 0 01-1 1A17 17 0 013 4a1 1 0 011-1h3.5a1 1 0 011 1 11 11 0 00.56 3.5 1 1 0 01-.25 1z" fill="#fff"/></svg></i>+1 (555) 014 2277</span>
  </div>
  <nav class="nav"><span>Home</span><span>About Us</span><span>Contact</span><span>Services</span><span>Blogs</span></nav>

  <div class="hero-panel"></div>
  <h1 class="hero-title">Turning your property into<br>a dream space</h1>
  <div class="btn btn-blue" style="left:112px;top:353px;width:204px;height:64px">Get Started</div>
</header>

<section>
  <h2 class="h2" style="top:752px">Services</h2>
  <p class="services-intro">Lorem ipsum dolor sit amet, consectetur adipiscing elit, sed do eiusmod tempor incididunt ut labore et dolore magna aliqua.</p>
  <svg class="arrows" style="left:1032px;top:852px" viewBox="0 0 56 16" aria-hidden="true">
    <path d="M2 8 H22 M2 8 L8 3 M2 8 L8 13" stroke="#141414" stroke-width="2.4" fill="none"/>
    <path d="M34 8 H54 M54 8 L48 3 M54 8 L48 13" stroke="#141414" stroke-width="2.4" fill="none"/>
  </svg>

  <div class="service" style="left:42px">
    <div class="service-glow"><div class="service-ring"><div class="service-core">
      <svg width="62" height="62" viewBox="0 0 62 62" fill="none" stroke="#0b57b5" stroke-width="2.6"><path d="M12 28 L31 12 L50 28 V46 H12 Z"/><rect x="26" y="26" width="10" height="10"/><path d="M6 50 Q20 44 30 50 L46 48 Q52 46 54 50"/></svg>
    </div></div></div>
    <div class="service-title">Staging for Realtors</div>
    <p class="service-text">Lorem ipsum dolor sit amet, consectetur adipiscing elit, sed do eiusmod tempor</p>
  </div>

  <div class="service" style="left:443px">
    <div class="service-glow"><div class="service-ring"><div class="service-core">
      <svg width="62" height="62" viewBox="0 0 62 62" fill="none" stroke="#0b57b5" stroke-width="2.6"><rect x="12" y="10" width="38" height="42"/><path d="M8 10 H54"/><path d="M12 12 Q22 30 16 50 M50 12 Q40 30 46 50"/><path d="M31 12 V52"/></svg>
    </div></div></div>
    <div class="service-title">Occupied Staging</div>
    <p class="service-text">Lorem ipsum dolor sit amet, consectetur adipiscing elit, sed do eiusmod tempor</p>
  </div>

  <div class="service" style="left:842px">
    <div class="service-glow"><div class="service-ring"><div class="service-core">
      <svg width="62" height="62" viewBox="0 0 62 62" fill="none" stroke="#0b57b5" stroke-width="2.6"><rect x="12" y="8" width="38" height="46"/><rect x="18" y="14" width="8" height="7"/><rect x="36" y="14" width="8" height="7"/><rect x="18" y="26" width="8" height="7"/><rect x="36" y="26" width="8" height="7"/><rect x="26" y="40" width="10" height="14"/></svg>
    </div></div></div>
    <div class="service-title">Staging for Apartments</div>
    <p class="service-text">Lorem ipsum dolor sit amet, consectetur adipiscing elit, sed do eiusmod tempor</p>
  </div>
</section>

<section class="about">
  <div class="about-glow" role="img" aria-label="Soft white paint splash texture"></div>
  <div class="brand brand-about">Loft 17<br>Design</div>
  <h2 class="about-title">ABOUT US</h2>
  <p class="about-text">Lorem ipsum dolor sit amet, consectetur adipiscing elit, sed do eiusmod tempor incididunt ut labore et dolore magna aliqua. Ut enim ad minim veniam, quis nostrud exercitation ullamco laboris nisi ut aliquip ex ea commodo consequat. Duis aute irure dolor in reprehenderit in voluptate velit esse cillum dolore eu fugiat nulla pariatur.</p>
  <div class="btn btn-white" style="left:881px;top:358px;width:206px;height:64px">Read More</div>
</section>

<section class="band" role="img" aria-label="Dark interior with plants behind the years badge">
  <div class="band-badge"></div>
  <p class="band-text">Have been in the design and furniture industry</p>
</section>

<section>
  <h2 class="h2" style="top:2195px">Gallery</h2>
  <div class="photo" style="left:112px;top:2267px;width:240px;height:278px;background:linear-gradient(160deg,#4a3a30,#9a6a45 50%,#3a3f50)" role="img" aria-label="Living room with stone fireplace and leather sofa"></div>
  <div class="photo" style="left:357px;top:2267px;width:241px;height:164px;background:linear-gradient(150deg,#5a4a3e,#c9b9a8 55%,#8a5a3e)" role="img" aria-label="Bed with striped cushions"></div>
  <div class="photo" style="left:357px;top:2435px;width:241px;height:110px;background:linear-gradient(150deg,#3a4a2e,#b8a88e 50%,#4a6a3a)" role="img" aria-label="Patio chair with potted plant"></div>
  <div class="photo" style="left:602px;top:2267px;width:126px;height:107px;background:linear-gradient(160deg,#d8d6d0,#5a5048)" role="img" aria-label="Dining table and chairs"></div>
  <div class="photo" style="left:731px;top:2267px;width:111px;height:107px;background:linear-gradient(160deg,#6a5a50,#3c6a3a)" role="img" aria-label="Leather armchair with plant"></div>
  <div class="photo" style="left:602px;top:2378px;width:119px;height:167px;background:linear-gradient(160deg,#e8e8e6,#7a7f7a 60%,#4a4a48)" role="img" aria-label="Open plan living room with ceiling fan"></div>
  <div class="photo" style="left:724px;top:2378px;width:118px;height:167px;background:linear-gradient(160deg,#5a5e62,#8a6a4a 55%,#3a3a3a)" role="img" aria-label="Stone fireplace living room"></div>
  <div class="photo" style="left:846px;top:2267px;width:241px;height:278px;background:linear-gradient(160deg,#f0f0ee,#d8d4cc 55%,#3a5a8a)" role="img" aria-label="Bright living room with tall windows and blue cushions"></div>
  <div class="btn btn-blue" style="left:497px;top:2583px;width:206px;height:65px">View More</div>
</section>

<section class="blogs">
  <h2 class="h2" style="top:90px;color:#fff">Blogs</h2>
  <svg class="arrows" style="left:1032px;top:92px" viewBox="0 0 56 16" aria-hidden="true">
    <path d="M2 8 H22 M2 8 L8 3 M2 8 L8 13" stroke="#fff" stroke-width="2.4" fill="none"/>
    <path d="M34 8 H54 M54 8 L48 3 M54 8 L48 13" stroke="#fff" stroke-width="2.4" fill="none"/>
  </svg>

  <article class="blog-card" style="left:100px">
    <div class="blog-photo" style="background:linear-gradient(160deg,#2e3a2a,#8a5a3e 50%,#d8d8d4)" role="img" aria-label="Dining table set with wine glasses"></div>
    <div class="blog-date">AUG<br>8</div>
    <p class="blog-text">Lorem ipsum dolor sit amet, consectetur adipiscing elit, sed do eiusmod tempor incididunt ut labore et dolore magna aliqua. <svg width="22" height="10" viewBox="0 0 22 10"><path d="M1 5 H20 M20 5 L15 1 M20 5 L15 9" stroke="#141414" stroke-width="2" fill="none"/></svg></p>
  </article>

  <article class="blog-card" style="left:638px">
    <div class="blog-photo" style="background:linear-gradient(160deg,#5a3a28,#cbb89a 50%,#2a2a2a)" role="img" aria-label="Game room with pool table and foosball table"></div>
    <div class="blog-date">AUG<br>8</div>
    <p class="blog-text">Lorem ipsum dolor sit amet, consectetur adipiscing elit, sed do eiusmod tempor incididunt ut labore et dolore magna aliqua. <svg width="22" height="10" viewBox="0 0 22 10"><path d="M1 5 H20 M20 5 L15 1 M20 5 L15 9" stroke="#141414" stroke-width="2" fill="none"/></svg></p>
  </article>
</section>

<footer class="footer">
  <div class="brand brand-footer"><span class="brand-dot"></span>Loft 17<br>Design</div>
  <div class="foot-contact" style="top:200px"><i class="foot-ico"><svg width="14" height="12" viewBox="0 0 14 12"><rect x="1" y="1" width="12" height="10" rx="1" fill="none" stroke="#0b57b5" stroke-width="1.6"/><path d="M1 2 L7 7 L13 2" fill="none" stroke="#0b57b5" stroke-width="1.6"/></svg></i>hello@loft17studio.com</div>
  <div class="foot-contact" style="top:242px"><i class="foot-ico"><svg width="14" height="14" viewBox="0 0 24 24"><path d="M6.6 10.8a15 15 0 006.6 6.6l2.2-2.2a1 1 0 011-.25 11 11 0 003.5.56 1 1 0 011 1V20a1 1 0 01-1 1A17 17 0 013 4a1 1 0 011-1h3.5a1 1 0 011 1 11 11 0 00.56 3.5 1 1 0 01-.25 1z" fill="#0b57b5"/></svg></i>+1 (555) 014 2277</div>

  <div class="foot-col" style="left:443px"><h3>Links</h3><p>Home<br>About Us<br>Contact<br>Services<br>Blogs</p></div>
  <div class="foot-col" style="left:651px"><h3>Location</h3><p>Lorem ipsum dolor sit amet<br>id est laborum</p></div>
  <div class="foot-col" style="left:988px"><h3>Follow Us</h3></div>
  <span class="social" style="top:115px"></span>
  <span class="social" style="top:166px"></span>
  <span class="social" style="top:218px"></span>

  <p class="copyright">Copyright @ 2023 - Loft 17 - All Rights Reserved</p>
</footer>

</body>
</html>
```